Web Design + logo Project

hi,
we are based in ASEAN region (Malaysia/Indonesia/Singapore), involving in Online Vehicle Insurance Portal. so far our product is only car insurance and personal insurance, and motorbikes insurance)
We need a webdesign + logo for TolaKover.com
The website is www.tolakover.example. The website is already up with the necessary quotation comparison + purchase mechanism.
We like www.brightlane.example look and feel very much.
Blue is the preferred main theme.
The mainpage should highlight the following
1) quotation generator/input
2) hotline number
3) news/testimonial
The webdesign should be able to cater for mobile users as well.
The design should be professional and energetic
Target Market(s)
20-35years old vehicle owners in Indonesia/thailand/Singapore/vietnam
Industry/Entity Type
Car Insurance
Look and feel

```html
<!DOCTYPE html>
<html lang="en">
<head>
<meta charset="utf-8">
<title>TolaKover.com – Vehicle Insurance</title>
<link rel="stylesheet" href="https://fonts.googleapis.com/css2?family=Arimo:wght@400;700&family=Fira+Sans:wght@300;400&display=swap">
<style>
:root{
  --brand:#1d4f8f;
  --nav-top:#3f8fd8;
  --nav-bottom:#1565b5;
  --accent:#f27a1e;
  --accent-dark:#d9600a;
  --sky-top:#dff0fa;
  --sky-bottom:#f6fbfe;
  --band-top:#7fc8e8;
  --band-bottom:#d9eff9;
  --ink:#2a2a2a;
  --link:#1d6fb8;
  --call:#2d5592;
  --footer:#9fb9d8;
  --footer-head:#1e3f7a;
  --rule:#4a78b4;
}
*{box-sizing:border-box;margin:0;padding:0}
html,body{width:1065px;height:1200px;overflow:hidden}
body{position:relative;font-family:"Arimo",Arial,sans-serif;color:var(--ink);
  background:linear-gradient(var(--sky-top),var(--sky-bottom) 340px,#fff 480px)}
.abs{position:absolute}
.top-bar{left:0;top:0;width:1065px;height:7px;background:var(--nav-bottom)}
.band{left:0;top:352px;width:1065px;height:130px;border-top:4px solid var(--nav-bottom);
  background:linear-gradient(var(--band-top),var(--band-bottom))}
.login{left:852px;top:16px;font-size:10px;color:var(--link);text-decoration:underline;display:flex;align-items:center;gap:4px}
.login i{width:10px;height:11px;border:1px solid #8a9bb0;border-radius:2px;display:block}
.logo{left:153px;top:42px;display:flex;align-items:center;gap:8px;font-size:22px;font-weight:700;color:var(--brand)}
.logo b{width:18px;height:18px;background:var(--brand);display:block}
.nav{left:347px;top:39px;width:591px;height:37px;display:flex;border-radius:3px;
  background:linear-gradient(var(--nav-top),var(--nav-bottom))}
.nav a{color:#fff;text-decoration:none;font-size:16px;display:flex;align-items:center;justify-content:center;border-right:1px solid #5d9fdc}
.nav a:last-child{border:0}
.hotline{left:741px;top:87px;width:200px;height:42px;border:3px solid var(--nav-bottom);border-radius:21px;background:#fff;
  text-align:center;padding-right:30px;line-height:1}
.hotline strong{display:block;color:var(--accent);font-size:20px;font-weight:400;margin-top:3px}
.hotline span{color:var(--brand);font-size:12px}
.hotline svg{position:absolute;right:5px;top:5px}
.tagline{left:150px;top:148px;width:360px;text-align:center;font-family:"Fira Sans",sans-serif;font-weight:300;font-size:29px;line-height:35px;color:#1e1e1e}
.hero{left:509px;top:78px;width:369px;height:202px;border-radius:40px 60px 0 0;
  background:linear-gradient(135deg,#b9c7d4,#e9d6c6 45%,#5a6470)}
.cards{left:140px;top:280px;width:785px;height:191px;display:flex;border-top:14px solid var(--nav-bottom);
  background:linear-gradient(#fff 40%,rgba(255,255,255,.2))}
.card{flex:1;position:relative;text-align:center;border-right:2px solid #7b9ab8}
.card:last-child{border:0}
.card .pic{margin:2px auto 0;height:96px;border-radius:8px}
.card p{color:var(--link);font-size:15.5px;line-height:15px;margin-top:8px;height:32px}
.btn{display:inline-block;background:linear-gradient(#ff9440,var(--accent-dark));color:#fff;font-size:16px;padding:4px 6px;border-radius:3px;box-shadow:0 1px 2px rgba(0,0,0,.3)}
.card .btn{margin-top:7px;width:124px}
.section-title{font-size:21px;font-weight:400;color:var(--link)}
.quote{left:144px;top:498px;width:441px}
.quote .section-title{border-bottom:2px solid #d8d8d8;padding-bottom:4px}
.form-row{position:absolute;left:1px;font-size:16px;color:#222;width:500px;height:24px}
.form-row label{position:absolute;left:0;top:2px}
.field{position:absolute;left:145px;width:272px;height:22px;border:1px solid #a9a9a9;font-size:13px;color:#999;padding:3px 13px;background:#fff}
.field i{position:absolute;right:1px;top:1px;width:24px;height:18px;background:#555}
.field i:after{content:"";position:absolute;left:7px;top:6px;border:5px solid transparent;border-top:6px solid #fff}
.radios{position:absolute;left:145px;top:0;display:flex;font-size:14.5px;color:#444}
.radios span{display:flex;align-items:center;gap:14px;margin-right:30px}
.radios i{width:14px;height:14px;border-radius:50%;border:1px solid #888;background:#eee;display:block}
.radios i.on{background:radial-gradient(#444 40%,#ddd 45%)}
.quote .btn{position:absolute;left:146px;top:205px;width:154px;font-size:16px}
.news{left:718px;top:498px;width:200px}
.news .section-title{color:#222;font-size:22px;margin-bottom:6px}
.news p{font-size:13px;line-height:16px;color:#333;margin-bottom:16px}
.badge{top:761px;height:38px;border-radius:4px}
.badge.one{left:512px;width:101px;background:#1e4d63}
.badge.two{left:643px;width:78px;border-radius:19px;background:#f0f0f0;border:2px solid #d9b72d}
.follow{left:762px;top:774px;font-size:10.5px;font-weight:700;color:var(--brand)}
.social{top:761px;width:38px;height:38px;border-radius:5px}
.social.one{left:845px;background:#5bbbe8}
.social.two{left:889px;background:#3a5a98}
.call{left:0;top:815px;width:1065px;height:50px;background:var(--call);color:#fff;font-size:28px;text-align:center;line-height:50px}
.footer{left:0;top:865px;width:1065px;height:335px;background:var(--footer)}
.col{position:absolute;top:28px;font-size:12px;line-height:15.7px;color:#fff;list-style:none}
.col h4{font-size:12px;font-weight:400;color:var(--footer-head);margin-bottom:7px;letter-spacing:.3px}
.rule{position:absolute;left:127px;width:810px;height:1px;background:var(--rule)}
.foot-logo{position:absolute;left:129px;top:230px;font-size:20px;font-weight:700;color:var(--brand);display:flex;align-items:center;gap:8px}
.foot-logo b{width:16px;height:16px;background:var(--brand);display:block}
.address{position:absolute;left:345px;top:227px;font-size:11.5px;line-height:16px;color:#fff}
.rights{position:absolute;left:0;width:1065px;top:298px;text-align:center;font-size:11.5px;color:var(--footer-head)}
</style>
</head>
<body>
<div class="abs top-bar"></div>
<div class="abs band"></div>

<a class="abs login"><i></i>customer login</a>
<div class="abs logo"><b></b>TolaKover.com</div>
<nav class="abs nav">
  <a style="width:93px">Home</a><a style="width:124px">Products</a><a style="width:118px">Services</a><a style="width:126px">About Us</a><a style="width:130px">Contact Us</a>
</nav>

<div class="abs hero" role="img" aria-label="Photo of a smiling young family with a child in front of a silver car"></div>
<div class="abs hotline"><strong>555-210-48</strong><span>Hot Line</span>
  <svg width="30" height="30" viewBox="0 0 30 30"><circle cx="15" cy="15" r="14" fill="#1565b5"/><circle cx="15" cy="15" r="11" fill="none" stroke="#fff" stroke-width="1.5"/><path d="M11 9c1-1 2 0 2.5 1.5s-.5 2-.5 2.5 2 4 3.5 4.5c.5.2 1-1 2-.8s2.5 1.3 1.5 2.5-2.5 1.5-4 .5-5-4.5-5.5-6.5 0-3.7.5-4.2z" fill="#fff"/></svg>
</div>
<h1 class="abs tagline">Take away the risk<br>and you can do anything.</h1>

<section class="abs cards">
  <div class="card"><div class="pic" role="img" aria-label="Photo of a black convertible sports car" style="width:187px;background:radial-gradient(#3a3a3a,#fff 75%)"></div>
    <p>We make our customers'<br>problems our problems.</p><span class="btn">Get Quote here</span></div>
  <div class="card"><div class="pic" role="img" aria-label="Photo of a father playing with his child outdoors" style="width:142px;background:radial-gradient(#d9b08f,#eaf2f6 75%)"></div>
    <p>Give your child an advantage<br>for life</p><span class="btn">Get Quote here</span></div>
  <div class="card"><div class="pic" role="img" aria-label="Photo of a silver sport motorbike" style="width:155px;background:radial-gradient(#9aa3ad,#fff 75%)"></div>
    <p>Enriching the lives of people<br>we touch</p><span class="btn">Get Quote here</span></div>
</section>

<section class="abs quote">
  <h2 class="section-title">Check Primium</h2>
  <div class="form-row" style="top:38px"><label>Type of Vehicle:</label><div class="field">----Select Type -----<i></i></div></div>
  <div class="form-row" style="top:68px"><label>&nbsp;Year:</label><div class="field">----Select Year -----<i></i></div></div>
  <div class="form-row" style="top:96px"><label>Price Assured:</label><div class="field">1000,000,000,000</div></div>
  <div class="form-row" style="top:130px"><label>Category:</label><div class="radios"><span><i class="on"></i>Personal</span><span><i></i>Service</span></div></div>
  <div class="form-row" style="top:162px"><label>Coverage:</label><div class="radios"><span style="margin-right:16px"><i class="on"></i>Total Loss Only</span><span><i></i>Comprehensive</span></div></div>
  <span class="btn">Check Questions</span>
</section>

<section class="abs news">
  <h2 class="section-title">Testimonial / News</h2>
  <p>we are based in ASEAN region (Malaysia/Indonesia/Singapore), involving in Online Vehicle Insurance Portal.</p>
  <p>so far our product is only car insurance and personal insurance, and motorbikes insurance)</p>
  <p>so far our product is only car insurance and personal insur-</p>
</section>

<div class="abs badge one" role="img" aria-label="Accreditation badge"></div>
<div class="abs badge two" role="img" aria-label="Security certificate badge"></div>
<div class="abs follow">FOLLOW US ON:</div>
<div class="abs social one" role="img" aria-label="Social network link"></div>
<div class="abs social two" role="img" aria-label="Social network link"></div>

<div class="abs call">Call 1-55-0100-777 to get Insured</div>

<footer class="abs footer">
  <ul class="col" style="left:126px"><h4>RECOMMENDED</h4><li>Meaning of Insurance</li><li>Home Insurance</li><li>Coverage Insurance</li><li>Ratings</li><li>Disability Insurance</li></ul>
  <ul class="col" style="left:284px"><h4>PROUDUCTS</h4><li>Car Insurance</li><li>Motor Bike Insurance</li><li>Personal Insurace</li></ul>
  <ul class="col" style="left:443px"><h4>SERCICES</h4><li>Demo Text</li><li>Car Insurance</li><li>Motor Bike Insurance</li><li>Personal Insurace</li></ul>
  <ul class="col" style="left:600px"><h4>FAQS</h4><li>Car Insurace</li><li>Motor Bike Insurance</li><li>Life Insurance</li></ul>
  <ul class="col" style="left:762px;top:30px"><h4>MORE INFORMATION</h4><li>Company Information</li><li>Management</li><li>Careers</li><li>Contact Us</li></ul>
  <div class="rule" style="top:193px"></div>
  <div class="foot-logo"><b></b>TOLAKOVER</div>
  <div class="address">Nusa Tower 9th Floor, Suite 904 | Jl. Merdeka Raya No. 18 | Jakarta 10110 | Indonesia<br>Phone: +62 21 5550 1234 | Fax: +62 21 5550 9876 | Samudra Media Group</div>
  <div class="rule" style="top:277px"></div>
  <div class="rights">All rights are reserved</div>
</footer>
</body>
</html>
```